My Book - Shattering the Vessel 2: Giants, Tombs, and the Ridge Alvoran Link, needs cover

I need a cover for the second book to wow potential readers. The book is non fiction and based on a plethora of research so the cover needs to evoke the high level of research involved while at the same time showcasing the exciting topic. I have attached the cover from my first book in this series. The new cover should draw on some themes from the first cover but be unique. Incorporating the themes of hybrids (human-angel), Hades (abode of the dead), and Ridge Alvoran (where Jesus was transfigured) should be woven in. I am very open to your artistic interpretation of those themes - in other words, you do not need to be on the nose with those. In the first cover, a stylized gene conveyed the idea of "angels, aliens, and the Antichrist revealed" quite well.

Target Market(s)

Christian, Bible Prophecy Lovers

Industry/Entity Type

Christian

Requirements
Must have
• The cover should have the same EDGY feel as my first cover (attached). It should use the same or very similar font. It must be the right size to print (TDB). While the content of the book is well researched, the audience popular Christian.
Nice to have
• Be creative with the themes.
Should not have
• This should not feel like a fiction book or "fantasy" book. It should not feel too "academic."

```html
<!DOCTYPE html>
<html lang="en">
<head>
<meta charset="utf-8">
<title>Shattering the Vessel – Cover Wrap</title>
<link href="https://fonts.googleapis.com/css2?family=Bebas+Neue&display=swap" rel="stylesheet">
<style>
  :root {
    --page-bg: #c9c9c9;
    --sky-top: #5e5e60;
    --sky-mid: #4d4947;
    --glow-warm: #9a7560;
    --glow-rose: #7a5a52;
    --ground: #151517;
    --panel: rgba(18, 18, 20, 0.86);
    --ink-light: #ffffff;
    --ink-body: #e2e2e2;
    --ink-sub: #d0d0d0;
    --ink-faint: #262628;
  }
  * { margin: 0; padding: 0; box-sizing: border-box; }
  html, body { width: 745px; height: 1200px; overflow: hidden; }
  body {
    background: var(--page-bg);
    font-family: "Bebas Neue", "Arial Narrow", sans-serif;
    position: relative;
  }
  .cover-wrap {
    position: absolute;
    left: 20px; top: 370px;
    width: 705px; height: 460px;
    overflow: hidden;
  }
  .cover-art {
    position: absolute; inset: 0;
    background:
      radial-gradient(ellipse 130px 150px at 540px 215px, rgba(170,128,104,0.85), rgba(154,117,96,0) 75%),
      radial-gradient(ellipse 300px 70px at 560px 200px, rgba(154,117,96,0.7), rgba(154,117,96,0) 80%),
      radial-gradient(ellipse 260px 60px at 330px 230px, rgba(122,90,82,0.55), rgba(122,90,82,0) 80%),
      radial-gradient(circle 26px at 395px 275px, rgba(150,120,100,0.35), rgba(150,120,100,0) 100%),
      radial-gradient(circle 22px at 250px 330px, rgba(140,115,100,0.3), rgba(140,115,100,0) 100%),
      radial-gradient(ellipse 200px 140px at 90px 20px, rgba(20,20,22,0.85), rgba(20,20,22,0) 80%),
      radial-gradient(ellipse 420px 120px at 360px 420px, rgba(12,12,14,0.9), rgba(12,12,14,0) 85%),
      linear-gradient(180deg, var(--sky-top) 0%, var(--sky-mid) 38%, #3a3434 58%, #242224 75%, var(--ground) 100%);
  }
  .back-panel {
    position: absolute;
    left: 32px; top: 26px;
    width: 270px; height: 380px;
    background: var(--panel);
    padding: 18px 18px 0 23px;
    color: var(--ink-light);
  }
  .back-title {
    font-size: 31px; line-height: 0.96; font-weight: 400;
  }
  .back-subtitle {
    font-size: 6px; margin: 3px 0 6px;
    color: var(--ink-sub);
  }
  .blurb p {
    font-size: 7.1px; line-height: 10.3px; color: var(--ink-body);
    text-align: justify; margin-bottom: 9px;
  }
  .back-author {
    position: absolute; left: 66px; top: 417px; width: 200px;
    text-align: center;
    font-size: 31px; line-height: 1; color: var(--ink-faint);
  }
  .spine-title, .spine-author {
    position: absolute;
    writing-mode: vertical-rl;
    color: var(--ink-light);
    white-space: nowrap;
    line-height: 1;
  }
  .spine-title { left: 338px; top: 46px; font-size: 31px; }
  .spine-author { left: 345px; top: 350px; font-size: 16px; }
  .front-title {
    position: absolute; left: 400px; top: 10px; width: 275px;
    text-align: center; color: var(--ink-light);
    font-size: 57px; line-height: 0.82; font-weight: 400;
  }
  .front-subtitle {
    position: absolute; left: 400px; top: 107px; width: 275px;
    text-align: center; color: var(--ink-sub); font-size: 11.5px;
  }
  .front-author {
    position: absolute; left: 400px; top: 432px; width: 275px;
    text-align: center; color: var(--ink-light); font-size: 23px; line-height: 1;
  }
</style>
</head>
<body>
  <section class="cover-wrap">
    <div class="cover-art" role="img" aria-label="Photograph of a wooden cross silhouetted against a hazy sunset glow above a dark hilltop, with soft bokeh lights"></div>

    <div class="back-panel">
      <h2 class="back-title">Shattering<br>the Vessel</h2>
      <div class="back-subtitle">Giants, Tombs, and the Ridge Alvoran Link</div>
      <div class="blurb">
        <p>Long before the flood, rebel watchers descended on a lonely summit and broke the boundary between heaven and earth. Their offspring, the giants of old, filled the land with violence and left behind tombs, legends and a trail of ruin that Scripture never forgot. From Genesis to Revelation the Bible hints at a hidden war over the image of God in man, a war fought on mountains, in valleys and in the depths below. This study follows that trail step by step, from the first rebellion on the heights to the final battle still to come, and shows why the story matters for every believer today.</p>
        <p>Why did the Lord choose that very mountain to reveal His glory before His chosen witnesses? What lies beneath the earth, in the realm of the dead, and who holds its keys? The answers may surprise you and will change how you read familiar passages.</p>
        <p>Drawing on ancient texts, archaeology, early Jewish writings and careful reading of the Bible, the author connects the giants, the gates of Hades and Ridge Alvoran into one clear story of conflict and victory. Every chapter is grounded in research yet written for every believer who loves prophecy and wants to understand the times. You will see how the enemy has always sought to twist what God made good, and how each attempt has failed. Along the way, forgotten details in the text come alive and long-standing questions finally find solid, biblical answers.</p>
        <p>Discover how the cross answers every corruption of the image, and why the war that began on a mountain will one day end on a mountain, with the King of Kings standing in victory.</p>
      </div>
    </div>
    <div class="back-author">Daniel Harrow</div>

    <div class="spine-title">Shattering the Vessel</div>
    <div class="spine-author">Daniel Harrow</div>

    <h1 class="front-title">Shattering<br>the Vessel</h1>
    <div class="front-subtitle">Giants, Tombs, and the Ridge Alvoran Link</div>
    <div class="front-author">Daniel Harrow</div>
  </section>
</body>
</html>
```